One label design for 3 different sizes of honey bottles

Our honey company -- Amber Hollow Apiary -- needs new product labels, integrating our new name and logo. We would like one label design that presents equally well on three different sizes of plastic honey bottles. Designs should include a front and back label.

Keep in mind that we really like our old label. Please submit designs that have a similar color and font scheme as the old label.

In the uploaded files, you will find (1) detailed content instructions for each size label (2 lb, 1 lb, 8 oz), (2) photo of three plastic bottles without labels, (3) *.ai file for the new company logo, and (4) image of old package label.

Requirements
Must have
• Same look and feel as our old label, but with our new name and logo

```html
<!DOCTYPE html>
<html lang="en">
<head>
<meta charset="utf-8">
<title>Amber Hollow Apiary – Honey Labels</title>
<link href="https://fonts.googleapis.com/css2?family=Open+Sans:wght@400;700&family=Rye&family=Special+Elite&display=swap" rel="stylesheet">
<style>
  :root {
    --ink: #3a3b35;
    --paper: #f7f0e2;
    --tan-soft: rgba(214, 190, 140, 0.35);
    --tan-faint: rgba(214, 190, 140, 0.22);
    --canvas: #ffffff;
  }
  html, body {
    margin: 0;
    padding: 0;
    width: 1200px;
    height: 1200px;
    overflow: hidden;
    background: var(--canvas);
  }
  .canvas {
    position: relative;
    width: 1200px;
    height: 1200px;
    color: var(--ink);
  }
  .label-art {
    position: absolute;
    inset: 0;
  }
  .frame-outer { fill: var(--paper); stroke: var(--ink); stroke-width: 3.5; }
  .frame-inner { fill: none; stroke: var(--ink); stroke-width: 2; }
  .title-band { fill: var(--paper); stroke: var(--ink); stroke-width: 3.5; }
  .title-band-inner { fill: none; stroke: var(--ink); stroke-width: 1.6; }
  .ornament { fill: var(--tan-soft); }
  .scene { fill: var(--tan-faint); }
  .title-word {
    font-family: "Rye", serif;
    font-size: 150px;
    fill: var(--ink);
  }
  .typewriter { font-family: "Special Elite", "Courier New", monospace; }
  .text {
    position: absolute;
    margin: 0;
    text-align: center;
  }
  .tagline {
    left: 97px; width: 436px; top: 254px;
    font-size: 27px; letter-spacing: 5px;
  }
  .brand-mark {
    left: 205px; width: 220px; top: 664px;
    font-size: 28px; line-height: 34px;
  }
  .net-weight {
    left: 97px; width: 436px; top: 928px;
    font-size: 22px; letter-spacing: 1px;
  }
  .promise {
    left: 690px; width: 374px; top: 352px;
    font-size: 21px; line-height: 28px;
  }
  .nutrition {
    position: absolute;
    left: 692px; width: 372px; top: 630px;
    font-family: "Open Sans", Arial, sans-serif;
    font-size: 13.6px; line-height: 18px;
    margin: 0;
  }
  .nutrition h2 {
    margin: 0 0 1px;
    font-size: 17px; line-height: 20px; font-weight: 700;
    letter-spacing: 0.4px;
  }
  .nutrition p { margin: 0; }
  .nutrition b { font-weight: 700; }
  .nutrition .footnote { font-size: 10.4px; line-height: 17px; margin-top: 1px; }
  .infant-warning {
    left: 692px; width: 374px; top: 834px;
    font-size: 11.6px; text-align: left; letter-spacing: 0.1px;
  }
  .address {
    left: 690px; width: 374px; top: 866px;
    font-size: 16.5px; line-height: 22px;
  }
</style>
</head>
<body>
<main class="canvas">
  <svg class="label-art" viewBox="0 0 1200 1200" width="1200" height="1200">
    <g class="label label--front" transform="translate(97 210)">
      <path class="frame-outer" d="M26 0 H410 A26 26 0 0 0 436 26 V754 A26 26 0 0 0 410 780 H26 A26 26 0 0 0 0 754 V26 A26 26 0 0 0 26 0 Z"/>
      <path class="frame-inner" d="M28 10 H408 A18 18 0 0 0 426 28 V752 A18 18 0 0 0 408 770 H28 A18 18 0 0 0 10 752 V28 A18 18 0 0 0 28 10 Z"/>
    </g>
    <g class="title-band-group">
      <rect class="title-band" x="62" y="323" width="506" height="164"/>
      <rect class="title-band-inner" x="69" y="330" width="492" height="150"/>
      <text class="title-word" x="76" y="464" textLength="478" lengthAdjust="spacingAndGlyphs">HONEY</text>
    </g>
    <rect class="ornament" x="127" y="492" width="108" height="84" rx="28" role="img" aria-label="Scrolled corner flourish"/>
    <rect class="ornament" x="395" y="492" width="108" height="84" rx="28" role="img" aria-label="Scrolled corner flourish"/>
    <rect class="scene" x="205" y="588" width="220" height="216" rx="24" role="img" aria-label="State outline with bee and forest scene behind the brand name"/>
    <rect class="ornament" x="127" y="816" width="108" height="86" rx="28" role="img" aria-label="Scrolled corner flourish"/>
    <rect class="ornament" x="395" y="816" width="108" height="86" rx="28" role="img" aria-label="Scrolled corner flourish"/>

    <g class="label label--back" transform="translate(659 210)">
      <path class="frame-outer" d="M26 0 H410 A26 26 0 0 0 436 26 V754 A26 26 0 0 0 410 780 H26 A26 26 0 0 0 0 754 V26 A26 26 0 0 0 26 0 Z"/>
      <path class="frame-inner" d="M28 10 H408 A18 18 0 0 0 426 28 V752 A18 18 0 0 0 408 770 H28 A18 18 0 0 0 10 752 V28 A18 18 0 0 0 28 10 Z"/>
    </g>
    <rect class="ornament" x="692" y="255" width="108" height="86" rx="28" role="img" aria-label="Scrolled corner flourish"/>
    <rect class="ornament" x="955" y="255" width="108" height="86" rx="28" role="img" aria-label="Scrolled corner flourish"/>
    <rect class="ornament" x="835" y="272" width="84" height="62" rx="20" role="img" aria-label="Honeybee illustration"/>
    <rect class="ornament" x="692" y="505" width="96" height="92" rx="28" role="img" aria-label="Scrolled corner flourish"/>
    <rect class="ornament" x="967" y="505" width="96" height="92" rx="28" role="img" aria-label="Scrolled corner flourish"/>
  </svg>

  <p class="text tagline typewriter">LOCAL • PURE • RAW</p>
  <p class="text brand-mark typewriter">Amber Hollow<br>Apiary</p>
  <p class="text net-weight typewriter">Net Wt. 2 LB (907 g)</p>

  <p class="text promise typewriter">Amber Hollow Apiary<br>promises 100% pure honey,<br>never pasteurized, and<br>sourced exclusively from<br>beehives we keep near<br>Maple Fork,<br>West Virginia</p>

  <section class="nutrition">
    <h2>NUTRITION FACTS</h2>
    <p>Servings: 43, <b>Serv. size: 1 Tbls (21g),</b><br>Amount per serving: <b>Calories 60, Total Fat</b> 0g (0% DV), Sat. Fat. 0g (0% DV), Trans Fat 0g, <b>Cholest.</b> 0mg (0% DV), <b>Sodium</b> 0mg (0% DV), <b>Total Carb.</b> 17g (6% DV), Fiber 0g (0% DV), Total Sugars 17g ( , 34% DV†), <b>Protein</b> 0g, Vit. D (0% DV), Calcium (0% DV), Iron (0% DV), Potas (0% DV).</p>
    <p class="footnote">† One serving adds 17g of sugar to your diet and represents 34% of the Daily Value for Added Sugars.</p>
  </section>

  <p class="text infant-warning typewriter">DO NOT FEED HONEY TO INFANTS UNDER ONE YEAR OLD</p>
  <p class="text address typewriter">Amber Hollow Apiary<br>18 Clover Ridge Lane<br>Maple Fork, WV 25000<br>www.amberhollowapiary.com</p>
</main>
</body>
</html>
```